Criminal Defense Law Firm needs Stationary design Theme for a Business Card, Envelope, and Letterhea

Our Law Firm is seeking a general design concept for a business card, letterhead, and Envelope.

Our website is WillowcrestTrialDesk.com

A design for these three items is requested to keep branding in place for the firm. Would like to keep the Firm Colors on the website consistent with our branding on business cards, letterheads, and mailing envelopes #10 size to be exact.

We would like business cards printed front and back with Law firm Colors from website.

Letterhead with law firm colors as well. Design is not limited to just the header, but the footer can be utilized as well for email, website, phone, fax, etc.

Simple #10 envelope consisting of the same design principles set out in the previous two designs.

```html
<!DOCTYPE html>
<html lang="en">
<head>
<meta charset="utf-8">
<title>Willowcrest Trial Desk – Stationery</title>
<link href="https://fonts.googleapis.com/css2?family=Crimson+Pro:wght@400;500&family=Montserrat:wght@600&family=Open+Sans:wght@400;600&display=swap" rel="stylesheet">
<style>
  :root {
    --backdrop: #575757;
    --paper: #ffffff;
    --ink: #1f1312;
    --gold: #9a885c;
    --faint: #f1ede6;
    --text: #231a18;
  }
  * { margin: 0; padding: 0; box-sizing: border-box; }
  html, body { width: 1200px; height: 1000px; overflow: hidden; }
  body { background: var(--backdrop); position: relative; font-family: "Open Sans", sans-serif; color: var(--text); }

  .sheet { position: absolute; background: var(--paper); overflow: hidden; box-shadow: 1px 2px 3px rgba(0,0,0,.45); }
  .sheet > svg.decor { position: absolute; inset: 0; width: 100%; height: 100%; }
  .band { fill: var(--ink); }
  .swoosh { fill: var(--gold); }
  .ghost-ring { fill: none; stroke: var(--faint); }

  .card-front { left: 121px; top: 21px; width: 435px; height: 255px; }
  .card-back { left: 121px; top: 321px; width: 435px; height: 254px; }
  .letterhead { left: 681px; top: 21px; width: 486px; height: 687px; }
  .envelope-front { left: 35px; top: 729px; width: 543px; height: 249px; }
  .envelope-back { left: 624px; top: 729px; width: 543px; height: 249px; }

  .holder-name { position: absolute; left: 40px; top: 62px; font-family: "Montserrat", sans-serif; font-weight: 600; font-size: 18px; color: var(--gold); letter-spacing: .3px; }
  .holder-role { position: absolute; left: 40px; top: 84px; font-size: 9.5px; color: var(--text); }

  .contact-list { position: absolute; list-style: none; }
  .contact-list li { display: flex; align-items: center; white-space: nowrap; }
  .contact-list .icon { display: inline-block; background: var(--gold); border-radius: 2px; flex: none; position: relative; }
  .contact-list .icon::after { content: ""; position: absolute; inset: 25%; border: 1px solid var(--paper); border-radius: 1px; }
  .card-front .contact-list { left: 200px; top: 142px; font-size: 10.5px; line-height: 14.4px; }
  .card-front .contact-list .icon { width: 10px; height: 10px; margin-right: 6px; }

  .firm-lockup { position: absolute; display: flex; align-items: center; }
  .firm-lockup .seal { border: 2px solid var(--ink); border-radius: 50%; flex: none; }
  .firm-name { font-family: "Crimson Pro", serif; font-weight: 500; color: var(--ink); text-transform: uppercase; letter-spacing: .5px; }
  .card-back .firm-lockup { left: 46px; top: 156px; }
  .card-back .seal { width: 56px; height: 56px; margin-right: 20px; }
  .card-back .firm-name { font-size: 20px; line-height: 23px; }

  .letterhead .firm-lockup { left: 33px; top: 46px; }
  .letterhead .seal { width: 37px; height: 37px; margin-right: 13px; border-width: 1.5px; }
  .letterhead .firm-name { font-size: 14px; line-height: 16px; }

  .letter-footer { position: absolute; left: 33px; top: 652px; display: flex; align-items: flex-start; font-size: 5.5px; line-height: 8px; }
  .letter-footer .signer { text-align: right; padding-right: 7px; margin-top: 5px; }
  .letter-footer .signer b { display: block; color: var(--gold); font-weight: 600; font-size: 6.5px; }
  .letter-footer .contact-list { position: static; border-left: 1px solid #999; padding: 0 7px; }
  .letter-footer .contact-list .icon { width: 5px; height: 5px; margin-right: 3px; background: var(--ink); }

  .envelope-front .firm-lockup { left: 30px; top: 165px; }
  .envelope-front .seal { width: 40px; height: 40px; margin-right: 11px; border-width: 1.5px; }
  .envelope-front .firm-name { font-size: 15px; line-height: 17px; }
  .envelope-front .contact-list { left: 82px; top: 209px; font-size: 6px; line-height: 8px; }
  .envelope-front .contact-list .icon { width: 6px; height: 6px; margin-right: 3px; background: var(--ink); }
  .envelope-front .return-address { position: absolute; left: 82px; top: 226px; font-size: 7px; font-weight: 600; }

  .flap-name { position: absolute; left: 0; right: 0; top: 30px; text-align: center; font-family: "Crimson Pro", serif; font-weight: 500; font-size: 13px; letter-spacing: 1px; text-transform: uppercase; color: var(--paper); }
</style>
</head>
<body>

<section class="sheet card-front" aria-label="Business card, front">
  <svg class="decor" viewBox="0 0 435 255" preserveAspectRatio="none" aria-hidden="true">
    <path class="band" d="M0 0H435V70Q300 28 0 42Z"/>
    <path class="swoosh" d="M200 46Q345 42 435 72V132Q365 66 200 46Z"/>
    <circle class="ghost-ring" cx="90" cy="140" r="62" stroke-width="5"/>
  </svg>
  <p class="holder-name">Marcus Hale</p>
  <p class="holder-role">Managing Director</p>
  <ul class="contact-list">
    <li><span class="icon"></span>0555.210.4867</li>
    <li><span class="icon"></span>0555.210.4867</li>
    <li><span class="icon"></span>0555.210.4867</li>
    <li><span class="icon"></span>contact@willowcrest.com</li>
    <li><span class="icon"></span>WillowcrestTrialDesk.com</li>
    <li><span class="icon"></span>14 Harrow Lane, Eastvale, WA, 6100</li>
  </ul>
</section>

<section class="sheet card-back" aria-label="Business card, back">
  <svg class="decor" viewBox="0 0 435 254" preserveAspectRatio="none" aria-hidden="true">
    <path class="band" d="M0 0H435V115Q300 20 0 90Z"/>
    <path class="swoosh" d="M190 52Q330 55 435 115V146Q360 75 190 52Z"/>
  </svg>
  <div class="firm-lockup">
    <span class="seal"></span>
    <p class="firm-name">Willowcrest Trial Desk<br>Law Offices</p>
  </div>
</section>

<section class="sheet letterhead" aria-label="Letterhead">
  <svg class="decor" viewBox="0 0 486 687" preserveAspectRatio="none" aria-hidden="true">
    <path class="band" d="M0 0H486V45Q300 18 0 24Z"/>
    <path class="swoosh" d="M210 24Q380 26 486 48V81Q400 42 210 24Z"/>
    <circle class="ghost-ring" cx="244" cy="384" r="114" stroke-width="6"/>
  </svg>
  <div class="firm-lockup">
    <span class="seal"></span>
    <p class="firm-name">Willowcrest Trial Desk<br>Law Offices</p>
  </div>
  <footer class="letter-footer">
    <p class="signer"><b>Owen Pritchard</b>Advocate</p>
    <ul class="contact-list">
      <li><span class="icon"></span>0555.210.4867</li>
      <li><span class="icon"></span>contact@willowcrest.com</li>
    </ul>
    <ul class="contact-list">
      <li><span class="icon"></span>WillowcrestTrialDesk.com</li>
      <li><span class="icon"></span>14 Harrow Lane, Eastvale, WA, 6100</li>
    </ul>
  </footer>
</section>

<section class="sheet envelope-front" aria-label="Envelope, front">
  <svg class="decor" viewBox="0 0 543 249" preserveAspectRatio="none" aria-hidden="true">
    <path class="band" d="M0 0H543V38Q330 8 0 48Z"/>
    <path class="swoosh" d="M235 26Q420 24 543 40V107Q450 36 235 26Z"/>
    <circle class="ghost-ring" cx="440" cy="190" r="54" stroke-width="4"/>
  </svg>
  <div class="firm-lockup">
    <span class="seal"></span>
    <p class="firm-name">Willowcrest Trial Desk<br>Law Offices</p>
  </div>
  <ul class="contact-list">
    <li><span class="icon"></span>0555.210.4867</li>
    <li><span class="icon"></span>contact@willowcrest.com</li>
  </ul>
  <p class="return-address">14 Harrow Lane, Eastvale, WA, 6100</p>
</section>

<section class="sheet envelope-back" aria-label="Envelope, back">
  <svg class="decor" viewBox="0 0 543 249" preserveAspectRatio="none" aria-hidden="true">
    <path class="swoosh" d="M0 0H543V52Q543 77 518 77H25Q0 77 0 52Z"/>
  </svg>
  <p class="flap-name">Willowcrest Trial Desk</p>
</section>

</body>
</html>
```